Accounting Practice Business Card Design

I have a logo I am happy for you to use in the design of the Business Card.
You can edit and change colours as you please, I am not fixated on it.
I am looking for a modern and clean overall feel for the finished design.

The business is a small accounting practice who thrives on word of mouth referrals and this card will be given to all current and prospect clients.

Industry/Entity Type

Accountant

Contact Information for Business Card

Marcus Vell
Level 5, 8 Ashcombe Ridge Road
FERNMOOR RISE VIC 3187
Phone: 9481 3052
Email: mvell@qrnaccountants.com.au
Web: www.qrnaccountants.com.au

Font styles to use
Serif
Sans Serif

Colors
0555a3
3277b5
85acd3
0393ce
33a6d7
85cae6
00a990
33b8a4
9bcb3c

Requirements
Must have
• "Clear answers to your tax worries start here"
• "Your recommendation means the most to our team"
Nice to have
• Modern clean professional

```html
<!DOCTYPE html>
<html lang="en">
<head>
<meta charset="utf-8">
<title>QRN Accountants – Business Card</title>
<link rel="stylesheet" href="https://fonts.googleapis.com/css2?family=Open+Sans:wght@400;600;700&display=swap">
<style>
  :root {
    --page-bg: #e6e7e9;
    --card-white: #fbfbfb;
    --navy: #14457f;
    --ink: #3a3a3a;
    --back-green: #2f7a3a;
    --back-text: #f4f7f4;
  }
  * { box-sizing: border-box; margin: 0; padding: 0; }
  html, body {
    width: 1200px;
    height: 960px;
    overflow: hidden;
    background: var(--page-bg);
    font-family: "Open Sans", Arial, sans-serif;
  }
  .stage {
    width: 1200px;
    height: 960px;
    display: flex;
    flex-direction: column;
    align-items: center;
    justify-content: center;
    gap: 40px;
  }
  .card {
    width: 688px;
    height: 420px;
    position: relative;
    box-shadow: 0 6px 18px rgba(0,0,0,0.18);
  }

  /* Front */
  .card-front { background: var(--card-white); color: var(--ink); }
  .brand-name {
    position: absolute;
    left: 36px;
    top: 52px;
    font-weight: 700;
    font-size: 34px;
    letter-spacing: 1px;
    color: var(--navy);
    text-transform: uppercase;
    line-height: 1;
  }
  .divider {
    position: absolute;
    left: 32px;
    right: 0;
    top: 108px;
    height: 2px;
    background: var(--navy);
    transform-origin: left center;
  }
  .person-name {
    position: absolute;
    right: 36px;
    top: 150px;
    font-weight: 700;
    font-size: 24px;
    letter-spacing: 1px;
    color: var(--navy);
    text-transform: uppercase;
    line-height: 1;
  }
  .name-rule {
    position: absolute;
    left: 380px;
    right: 0;
    top: 186px;
    height: 2px;
    background: var(--navy);
  }
  .contact {
    position: absolute;
    left: 36px;
    top: 222px;
    font-size: 17px;
    line-height: 1.45;
  }
  .address {
    position: absolute;
    right: 36px;
    bottom: 36px;
    font-size: 18px;
    line-height: 1.4;
    text-align: right;
  }

  /* Back */
  .card-back {
    background: var(--back-green);
    color: var(--back-text);
    display: flex;
    flex-direction: column;
    align-items: center;
    justify-content: center;
  }
  .back-brand {
    font-weight: 700;
    font-size: 96px;
    letter-spacing: 2px;
    line-height: 1;
    color: var(--back-text);
  }
  .tagline {
    margin-top: 40px;
    font-weight: 400;
    font-size: 17px;
    line-height: 1.5;
    text-align: center;
  }
</style>
</head>
<body>
  <main class="stage">
    <section class="card card-back" aria-label="Business card back">
      <div class="back-brand">QRN</div>
      <p class="tagline">Clear answers to your tax worries start here<br>Your recommendation means the most to our team</p>
    </section>

    <section class="card card-front" aria-label="Business card front">
      <div class="brand-name">QRN Accountants</div>
      <div class="divider"></div>
      <div class="person-name">Marcus Vell</div>
      <div class="name-rule"></div>
      <div class="contact">
        <p>P : 9481 3052</p>
        <p>mvell@qrnaccountants.com.au</p>
        <p>www.qrnaccountants.com.au</p>
      </div>
      <div class="address">
        <p>Level 5, 8 Ashcombe</p>
        <p>Ridge Road</p>
        <p>FERNMOOR RISE VIC 3187</p>
      </div>
    </section>
  </main>
</body>
</html>
```